Business card design for online Mandarin Learning School

We need a business card design for our online language learning school called "Maple Bridge Online for Mandarin Learning". Our existing website is https://www.maplebridgeonline.com
We have our logo already. We would like to see our business card design that can make our online teaching services to be innovative, young, energetic and fun to learn. Prefer to have a certain level of color matching with our website. Apart from "Maple Bridge Online", need to specifically state "for Mandarin Learning" as well on the business card.

```html
<!DOCTYPE html>
<html lang="en">
<head>
<meta charset="utf-8">
<title>Maple Bridge Online for Mandarin Learning – Business Card</title>
<link href="https://fonts.googleapis.com/css2?family=Cinzel:wght@400&family=Source+Serif+4:wght@400;700&display=swap" rel="stylesheet">
<style>
  :root {
    --teal: #12acb8;
    --coral: #e35f5f;
    --grey: #8a8a8a;
    --white: #ffffff;
    --backdrop: #dcdcdc;
    --card-shadow: 0 3px 5px rgba(0,0,0,0.35);
  }
  * { margin: 0; padding: 0; box-sizing: border-box; }
  html, body {
    width: 1125px;
    height: 1200px;
    overflow: hidden;
    background: var(--backdrop);
  }
  .card {
    position: absolute;
    left: 171px;
    width: 826px;
    height: 472px;
    border-radius: 22px;
    overflow: hidden;
    box-shadow: var(--card-shadow);
    font-family: "Source Serif 4", Georgia, serif;
  }
  .card-front { top: 106px; background: var(--white); }
  .card-back { top: 640px; background: var(--teal); }

  .front-waves {
    position: absolute;
    inset: 0;
    width: 100%;
    height: 100%;
  }

  .brand-mark {
    position: absolute;
    left: 0;
    width: 452px;
    top: 72px;
    text-align: center;
  }
  .brand-dot {
    display: block;
    width: 80px;
    height: 80px;
    margin: 0 auto 40px;
    border-radius: 50%;
    background: var(--coral);
  }
  .brand-name {
    font-family: "Cinzel", "Times New Roman", serif;
    font-size: 45px;
    font-weight: 400;
    letter-spacing: 1px;
    color: var(--teal);
    line-height: 1;
  }
  .brand-tagline {
    font-family: "Cinzel", "Times New Roman", serif;
    font-size: 17px;
    letter-spacing: 2px;
    color: var(--grey);
    margin-top: 10px;
    line-height: 1;
  }

  .contact-block {
    position: absolute;
    right: 37px;
    top: 198px;
    text-align: right;
    color: var(--white);
  }
  .person-name {
    font-size: 32px;
    font-weight: 700;
    line-height: 1;
    letter-spacing: 0.3px;
  }
  .person-title {
    font-size: 20px;
    line-height: 1;
    margin-top: 10px;
    letter-spacing: 0.5px;
  }
  .contact-list {
    list-style: none;
    margin-top: 14px;
  }
  .contact-item {
    display: flex;
    justify-content: flex-end;
    align-items: center;
    gap: 10px;
    font-size: 19.5px;
    height: 26.4px;
  }
  .contact-icon {
    width: 20px;
    height: 20px;
    fill: var(--white);
    flex: none;
  }
  .contact-address {
    font-size: 19.5px;
    margin-top: 11px;
    letter-spacing: 0.2px;
  }

  .back-brand {
    position: absolute;
    left: 0;
    right: 0;
    top: 118px;
    text-align: center;
  }
  .back-brand .brand-dot {
    width: 56px;
    height: 56px;
    background: var(--white);
    margin-bottom: 28px;
  }
  .back-brand .brand-name {
    color: var(--white);
    font-size: 54px;
  }
  .back-brand .brand-tagline {
    color: var(--white);
    font-size: 20px;
    margin-top: 14px;
  }

  .social-row {
    position: absolute;
    left: 0;
    right: 0;
    top: 403px;
    display: flex;
    justify-content: center;
    align-items: center;
    gap: 4px;
  }
  .social-rule {
    width: 70px;
    height: 1px;
    background: linear-gradient(to right, rgba(255,255,255,0), rgba(255,255,255,0.9));
  }
  .social-rule.is-right {
    background: linear-gradient(to left, rgba(255,255,255,0), rgba(255,255,255,0.9));
  }
  .social-slot {
    width: 24px;
    height: 24px;
    border: 2px solid var(--white);
    border-radius: 50%;
  }
</style>
</head>
<body>

<section class="card card-front" aria-label="Business card front">
  <svg class="front-waves" viewBox="0 0 800 457" preserveAspectRatio="none" aria-hidden="true">
    <path fill="var(--grey)" d="M505,162 C600,85 715,62 800,72 L800,112 C705,92 605,112 505,162 Z"/>
    <path fill="var(--coral)" d="M0,282 C70,330 200,352 318,318 C215,362 80,352 0,322 Z"/>
    <path fill="var(--teal)" d="M0,342 C120,385 255,372 385,240 C480,145 625,85 800,125 L800,457 L0,457 Z"/>
  </svg>

  <div class="brand-mark">
    <span class="brand-dot"></span>
    <div class="brand-name">MAPLE BRIDGE</div>
    <div class="brand-tagline">for Mandarin Learning</div>
  </div>

  <div class="contact-block">
    <div class="person-name">DANIEL CARTER</div>
    <div class="person-title">CEO/FOUNDER</div>
    <ul class="contact-list">
      <li class="contact-item">555 214 3867
        <svg class="contact-icon" viewBox="0 0 24 24" aria-label="Phone"><path d="M6.6 10.8a15.1 15.1 0 0 0 6.6 6.6l2.2-2.2c.3-.3.7-.4 1-.2 1.1.4 2.3.6 3.6.6.6 0 1 .4 1 1V20c0 .6-.4 1-1 1A17 17 0 0 1 3 4c0-.6.4-1 1-1h3.5c.6 0 1 .4 1 1 0 1.3.2 2.5.6 3.6.1.3 0 .7-.2 1z"/></svg>
      </li>
      <li class="contact-item">555 390 7152
        <svg class="contact-icon" viewBox="0 0 24 24" aria-label="Mobile"><path d="M7 1h10a2 2 0 0 1 2 2v18a2 2 0 0 1-2 2H7a2 2 0 0 1-2-2V3a2 2 0 0 1 2-2zm0 3v15h10V4zm5 16.2a1 1 0 1 0 0 .1z"/></svg>
      </li>
      <li class="contact-item">555 628 4019
        <svg class="contact-icon" viewBox="0 0 24 24" aria-label="Fax"><path d="M7 2h10v6H7zM3 9h18a1 1 0 0 1 1 1v8h-4v-4H6v4H2v-8a1 1 0 0 1 1-1zm4 6h10v7H7z"/></svg>
      </li>
      <li class="contact-item">info@maplebridgeonline.com
        <svg class="contact-icon" viewBox="0 0 24 24" aria-label="Email"><path d="M2 5h20v14H2zm2 2v.5l8 5 8-5V7l-8 5z"/></svg>
      </li>
      <li class="contact-item">www.maplebridgeonline.com
        <svg class="contact-icon" viewBox="0 0 24 24" aria-label="Website"><path d="M12 2a10 10 0 1 0 0 20 10 10 0 0 0 0-20zm-1 17.9A8 8 0 0 1 4.2 10L9 14.8v1a2 2 0 0 0 2 2zm6.9-2.5A2 2 0 0 0 16 16h-1v-3a1 1 0 0 0-1-1H8v-2h2a1 1 0 0 0 1-1V7h2a2 2 0 0 0 2-2v-.4a8 8 0 0 1 2.9 12.8z"/></svg>
      </li>
    </ul>
    <div class="contact-address">2140 Willow Lane, Anchorage, Alaska 99501</div>
  </div>
</section>

<section class="card card-back" aria-label="Business card back">
  <div class="back-brand">
    <span class="brand-dot"></span>
    <div class="brand-name">MAPLE BRIDGE</div>
    <div class="brand-tagline">for Mandarin Learning</div>
  </div>
  <div class="social-row">
    <span class="social-rule"></span>
    <span class="social-slot"></span>
    <span class="social-slot"></span>
    <span class="social-slot"></span>
    <span class="social-rule is-right"></span>
  </div>
</section>

</body>
</html>
```